Pelbrook Business Cards

Create new business cards with the details below.

Aaron Velst
Director

MB: +61 412 563 904
PH: 1300 417 639
Email: aaron.velst@pelbrook.com.au
Address: 27C Marlow Parade, Dunmere VIC 3925 Australia
Website: www.pelbrook.com.au

Target Market(s)

Other business

Industry/Entity Type

Business

Requirements
Must have
• must be clean looking

```html
<!DOCTYPE html>
<html lang="en">
<head>
<meta charset="utf-8">
<title>Pelbrook Business Cards</title>
<link rel="stylesheet" href="https://fonts.googleapis.com/css2?family=Didact+Gothic&display=swap">
<style>
  :root {
    --backdrop-light: #b3b3b3;
    --backdrop-dark: #6f6f6f;
    --card: #ffffff;
    --ink-dark: #2f2f2f;
    --ink-soft: #6a6a6a;
    --accent-green: #9bc53d;
    --card-shadow: rgba(0, 0, 0, 0.28);
  }
  * { box-sizing: border-box; margin: 0; padding: 0; }
  html, body {
    width: 1200px;
    height: 1000px;
    overflow: hidden;
  }
  body {
    position: relative;
    background: linear-gradient(180deg, var(--backdrop-light) 0%, var(--backdrop-dark) 100%);
    font-family: "Didact Gothic", "Century Gothic", sans-serif;
  }
  .card {
    position: absolute;
    width: 525px;
    height: 300px;
    background: var(--card);
    box-shadow: 0 18px 40px var(--card-shadow);
  }
  .card--back { left: 60px; top: 170px; }
  .card--front { left: 615px; top: 530px; }

  /* Back: contact details */
  .contact {
    position: absolute;
    left: 58px;
    bottom: 40px;
    padding-left: 18px;
    border-left: 3px solid var(--accent-green);
    list-style: none;
    color: var(--ink-soft);
    font-size: 14.5px;
    line-height: 1.42;
    letter-spacing: 0.2px;
    white-space: nowrap;
  }

  /* Front: brand and person */
  .brand {
    position: absolute;
    left: 42px;
    top: 118px;
    display: flex;
    align-items: center;
    gap: 16px;
  }
  .brand__mark {
    width: 44px;
    height: 44px;
    background: var(--accent-green);
  }
  .brand__name {
    color: var(--ink-dark);
    font-size: 52px;
    line-height: 1;
    letter-spacing: 1px;
  }
  .person {
    position: absolute;
    right: 40px;
    top: 150px;
    padding-left: 14px;
    border-left: 3px solid var(--accent-green);
    color: var(--ink-soft);
    font-size: 19px;
    line-height: 1.3;
  }
</style>
</head>
<body>
  <section class="card card--back" aria-label="Business card back">
    <ul class="contact">
      <li>MB: +61 412 563 904</li>
      <li>PH: 1300 417 639</li>
      <li>Email: aaron.velst@pelbrook.com.au</li>
      <li>Address: 27C Marlow Parade, Dunmere VIC 3925 Australia</li>
      <li>Website: www.pelbrook.com.au</li>
    </ul>
  </section>

  <section class="card card--front" aria-label="Business card front">
    <div class="brand">
      <span class="brand__mark" aria-hidden="true"></span>
      <span class="brand__name">Pelbrook</span>
    </div>
    <div class="person">
      <p class="person__name">Aaron Velst</p>
      <p class="person__role">Director</p>
    </div>
  </section>
</body>
</html>
```